real estate managers brochure A5

Real estate services brochure (owners corporation management)

Content has been uploaded in MS word documents and we reserve the right to refine the text in one revision.

Visit out site http://www.thebrellows.com.au/body-corporate-managers/ and review the pages in the 'owners corporation' menu in our website - the brochure is for these services we provide.

We want to showcase a variety of 'trophy' buildings/unit/apartment/factory developments that we manage - I've uploaded these 'case studies' and high res images for each.

Some General services photos to be provided by you.

The brochure is given out to potential owners who we wish to be clients.

We are going to print a few dozen of these in hard copy so will need artwork in nigh resolution pdf format and a web resolution version for emailing potential clients.

Target Market(s)

Unit owners, apartment owners and commercial factory owners

Industry/Entity Type

Property Management

Font styles to use
Serif
Sans Serif

Requirements
Must have
• A modern design that looks like it could be just as home on a website or facebook post
• Have a flair of retro design and/or vintage graphics
• 3 full pages of example properties we manage property. see example properties in the case studies. I have uploaded high res images for the full page images and some brief text for these pages
Should not have
• Must not look like a typical real estate agents brochure (smiling agents, happy home owners)
• Images of people who do not look australian (ie afro american, asian) as this is not our target market. We typically have anglo australian or eruopean looking clients
• We are a young company who pride ourselves on. Efficient services and high tech management systems for the properties we manage

```html
<!DOCTYPE html>
<html lang="en">
<head>
<meta charset="utf-8">
<title>Brellow – Why choose us</title>
<link href="https://fonts.googleapis.com/css2?family=PT+Sans:wght@400;700&display=swap" rel="stylesheet">
<style>
:root{
  --brand-blue:#2c4a9e;
  --heading-blue:#2a47a3;
  --text:#2f2f2f;
  --row-bg:#dcd9e2;
  --page-warm:#f7f1ec;
  --white:#ffffff;
}
*{margin:0;padding:0;box-sizing:border-box}
html,body{width:1200px;height:929px;overflow:hidden;background:var(--white)}
body{font-family:"PT Sans",sans-serif;color:var(--text)}
.spread{position:relative;width:1200px;height:929px;overflow:hidden;
  background:linear-gradient(180deg,#fbf8f5 0%,var(--page-warm) 45%,#f4eee9 75%,#fbfaf8 100%)}
.header-band{position:absolute;left:0;top:0;width:1200px;height:82px;background:var(--brand-blue)}
.header-band h1{position:absolute;top:22px;font-weight:400;font-size:29px;color:var(--white);letter-spacing:.1px}
.title-why{left:39px}
.title-accred{left:629px}
.header-rule{position:absolute;left:8px;right:8px;top:90px;border-top:2px dashed var(--brand-blue)}

.reason{position:absolute;left:0;width:600px}
.reason .badge{position:absolute;left:38px;width:46px;height:46px;border-radius:50%;
  background:var(--brand-blue);border:3px solid #fff;box-shadow:0 0 0 2px #e6e3ea;
  color:#fff;font-weight:700;font-size:17px;display:flex;align-items:center;justify-content:center}
.reason h2{margin-left:101px;font-size:19px;line-height:21px;font-weight:700;color:var(--heading-blue);width:470px}
.reason ul{list-style:none;margin:9px 0 0 101px;width:458px;font-size:14.6px;line-height:18.4px}

.accreditations{position:absolute;left:622px;top:111px;width:556px}
.accred-row{display:flex;background:var(--row-bg);margin-bottom:4px;padding:8px 0 8px 25px;font-size:14.8px;line-height:20px}
.accred-row dt{width:296px;font-weight:700}
.accred-row dd{flex:1}
.accred-row.fade{background:linear-gradient(180deg,var(--row-bg) 0%,rgba(220,217,226,.5) 55%,rgba(220,217,226,0) 100%);padding-bottom:60px}
.accred-row dd p+p{margin-top:20px}
.small-url{font-size:13.4px}

.team-photo{position:absolute;left:620px;top:520px;width:330px;height:409px;
  background:linear-gradient(180deg,rgba(247,241,236,0) 0%,#d9c9bd 18%,#b9a496 45%,#cfc2b8 80%,rgba(247,241,236,.6) 100%);
  border-radius:40% 40% 8px 8px / 18% 18% 4px 4px;opacity:.75}

.indemnity{position:absolute;left:949px;top:593px;width:251px;height:336px;background:var(--brand-blue);color:var(--white)}
.indemnity-frame{position:absolute;left:16px;top:16px;right:0;bottom:30px;border:2px dashed #fff;border-right:none}
.indemnity h3{position:absolute;left:35px;top:38px;font-size:15.5px;line-height:21px;font-weight:700;width:190px}
.indemnity p{position:absolute;left:35px;top:98px;font-size:14px;line-height:21.8px;width:180px}
</style>
</head>
<body>
<main class="spread">
  <header class="header-band">
    <h1 class="title-why">Why choose BRELLOW?</h1>
    <h1 class="title-accred">Accreditations &amp; affiliations</h1>
  </header>
  <div class="header-rule"></div>

  <section class="reason" style="top:122px">
    <span class="badge" style="top:2px">1</span>
    <h2>Fast, action orientated issue resolution</h2>
    <ul>
      <li>• BRELLOW's in-house proprietary systems and procedures ensure a swift response to your owners corporation issues.</li>
      <li>• When you choose BRELLOW you have access to our database of over 200+ contractors and suppliers.</li>
    </ul>
  </section>

  <section class="reason" style="top:257px">
    <span class="badge" style="top:4px">2</span>
    <h2>Effective, clear communication to all Stakeholders</h2>
    <ul>
      <li>o Communications procedure for managing contractors and ensuring timely responses</li>
      <li>o Diverse range of communication tools available – email, mail outs, websites, newsletters</li>
      <li>o Regular updates of key issues affecting Lot owners</li>
    </ul>
  </section>

  <section class="reason" style="top:409px">
    <span class="badge" style="top:3px">3</span>
    <h2>High tech solutions for efficient Owners corporation management</h2>
    <ul>
      <li>• State of the art computer systems for managing financial reporting, tracking of maintenance, keeping accounts and issuing statutory fee notices</li>
      <li>• Commitment to forward-thinking and evolving technology so we can provide the most efficient service for you</li>
      <li>• Online portal to access owners corporation records as required</li>
    </ul>
  </section>

  <section class="reason" style="top:604px">
    <span class="badge" style="top:2px">4</span>
    <h2>Unique expertise</h2>
    <ul>
      <li>• Qualified and experienced Owners Corporation Managers AND Real Estate Agents</li>
      <li>• Broad knowledge of legislation affecting owners corporations. We guide your decisions to ensure compliance with the Owners Corporation Act and Regulations</li>
    </ul>
  </section>

  <section class="reason" style="top:757px">
    <span class="badge" style="top:5px">5</span>
    <h2>Proven systems and procedures</h2>
    <ul>
      <li>• Timely reporting to your committee and at owners corporation meetings</li>
      <li>• BRELLOW's established checklist procedures and quality control systems</li>
      <li>• Many ways for owners to pay fee notices including bill pay, Direct debit, cheque, cash, credit card and eftpos</li>
    </ul>
  </section>

  <div class="team-photo" role="img" aria-label="Photo of three colleagues in business attire reviewing a blue folder in a bright office"></div>

  <dl class="accreditations">
    <div class="accred-row"><dt>Licenced Owners Corporation Managers</dt><dd>004512</dd></div>
    <div class="accred-row"><dt>Licenced Estate Agents</dt><dd>058914K</dd></div>
    <div class="accred-row"><dt>Property Institute of Victoria Member</dt><dd>Owners Corporation Chapter</dd></div>
    <div class="accred-row"><dt>Authorised Representative for:</dt><dd>Harbourline Cover<br>www.harbourlinecover.com.au</dd></div>
    <div class="accred-row fade"><dt>Insurance distributor for:</dt><dd>
      <p>Northgate Mutual<br>www.northgatemutual.com.au</p>
      <p>Parcel Unit Underwriters<br>www.parcelunit.com.au</p>
      <p>Commons Cover Insurance<br><span class="small-url">www.commonscover.com.au</span></p>
    </dd></div>
  </dl>

  <aside class="indemnity">
    <div class="indemnity-frame"></div>
    <h3>Professional Indemnity Insurance</h3>
    <p>Brellow Estate Agents carry $2 million Professional Indemnity insurance in excess of the prescribed amount under Section 119(5) of the Owners Corporation Act.</p>
  </aside>
</main>
</body>
</html>
```